Brightmark Pixel Collective Website

I need my website redesigned to look very modern with the latest services. Check out my old website for information: www.brightmarkpixelcollective.com

You can use the same site menu links

It doesn't need to have the Recent News section

Please use the yellow, black and grey color scheme

Target Market(s)

25-50 years in range. Small Business Owners

Industry/Entity Type

Group

Requirements
Must have
• Logo and similar color scheme to current website
• Modern, Modern, Modern! I want a very fresh and modern look
Should not have
• Boring Look

```html
<!DOCTYPE html>
<html lang="en">
<head>
<meta charset="utf-8">
<title>Brightmark Pixel Collective</title>
<link href="https://fonts.googleapis.com/css2?family=Lato:wght@300;400;700&family=Mulish:wght@300;400&display=swap" rel="stylesheet">
<style>
:root{
  --yellow:#f7a81b;
  --yellow-soft:#fbb828;
  --ink:#2b2b2b;
  --topbar:#1c1c1c;
  --header:#2a2a2a;
  --grey-bg:#f2f2f2;
  --text-grey:#9a9a9a;
  --nav-grey:#bdbdbd;
  --white:#ffffff;
}
*{box-sizing:border-box;margin:0;padding:0}
html,body{width:887px;height:1200px;overflow:hidden}
body{font-family:"Lato",sans-serif;background:var(--white);color:var(--ink);position:relative}
.abs{position:absolute}
h1,h2,h3{font-weight:400}

/* top bar */
.topbar{left:0;top:0;width:887px;height:26px;background:var(--topbar);color:#e0e0e0;font-size:8.5px}
.topbar .item{position:absolute;top:7px;display:flex;align-items:center;gap:6px;white-space:nowrap;line-height:12px}
.topbar svg{width:14px;height:11px;flex:none}

/* header */
.site-header{left:0;top:26px;width:887px;height:62px;background:var(--header)}
.brand{position:absolute;left:103px;top:14px;width:120px;display:flex;flex-direction:column;align-items:center;gap:4px}
.brand-mark{width:14px;height:14px;background:var(--yellow)}
.brand-name{font-family:"Lato",sans-serif;font-weight:400;font-size:8px;line-height:9px;color:var(--white);text-align:center;letter-spacing:.2px;white-space:nowrap}
.nav{position:absolute;top:0;left:0;width:887px;height:62px;font-size:10px;color:var(--nav-grey)}
.nav a{position:absolute;top:25px;color:inherit;text-decoration:none;white-space:nowrap}
.nav a.active{color:var(--yellow)}
.nav a.active::before{content:"";position:absolute;left:-3px;right:-3px;top:-25px;height:2px;background:var(--yellow)}
.caret{display:inline-block;width:4px;height:4px;border-right:1px solid currentColor;border-bottom:1px solid currentColor;transform:rotate(45deg);margin-left:4px;position:relative;top:-2px}

/* hero */
.hero{left:0;top:88px;width:887px;height:307px;background:linear-gradient(90deg,#4e4d4b 0%,#7a7874 30%,#8d8b87 55%,#6c6a66 80%,#4a4846 100%)}
.hero-shade{left:0;top:88px;width:887px;height:307px;background:rgba(0,0,0,.28)}
.hero-title{left:0;top:142px;width:887px;text-align:center;font-family:"Mulish",sans-serif;font-weight:300;color:var(--white);font-size:23px;line-height:28px}
.hero-btn{left:376px;top:270px;width:127px;height:31px;border:1px solid var(--yellow);color:var(--yellow);font-family:"Mulish",sans-serif;font-size:14px;display:flex;align-items:center;justify-content:center}

/* welcome */
.welcome{left:0;top:395px;width:887px;height:388px;background:var(--grey-bg)}
.section-title{width:887px;left:0;text-align:center;font-weight:300;color:#3a3a3a}
.welcome-title{top:430px;font-size:21px}
.welcome-lead{left:283px;top:468px;width:320px;text-align:center;font-size:9px;line-height:13px;color:var(--text-grey)}
.card{top:526px;width:200px}
.card-photo{height:122px;width:200px}
.card-title{margin-top:11px;font-size:10px;font-weight:400;color:#333}
.card-text{margin-top:6px;font-size:8.5px;line-height:13.5px;color:var(--text-grey)}
.card.featured .card-photo{outline:1px solid var(--yellow);border-bottom:4px solid var(--yellow);position:relative}
.card.featured .card-title{color:var(--yellow);font-weight:400}
.corner{position:absolute;right:0;bottom:-17px;width:0;height:0;border-left:13px solid transparent;border-top:13px solid var(--yellow)}
.plus{position:absolute;left:80px;top:45px;width:33px;height:33px;border-radius:50%;background:var(--yellow-soft);opacity:.9;display:flex;align-items:center;justify-content:center;color:#fff;font-size:18px;font-weight:300}

/* experts */
.experts-title{top:828px;font-size:20px}
.expert{top:890px;width:160px;text-align:center}
.expert-icon{width:61px;height:61px;border-radius:50%;background:var(--ink);margin:0 auto;display:flex;align-items:center;justify-content:center}
.expert-icon svg{width:32px;height:32px}
.expert.featured .expert-icon{background:var(--yellow-soft)}
.expert-title{margin-top:22px;font-size:14px;font-weight:400;color:#222;white-space:nowrap}
.expert.featured .expert-title{color:var(--yellow)}
.expert-text{margin-top:6px;font-size:8.5px;line-height:13.5px;color:var(--text-grey);padding:0 6px}
.expert-btn{position:absolute;top:211px;left:46px;width:69px;height:20px;border:1px solid var(--yellow);font-size:7.5px;color:#555;display:flex;align-items:center;justify-content:center}
.expert.featured .expert-btn{border-color:#333;color:#222}
.footer-band{left:0;top:1180px;width:887px;height:20px;background:var(--grey-bg)}
</style>
</head>
<body>

<div class="abs topbar">
  <div class="item" style="left:109px">
    <svg viewBox="0 0 14 11"><rect x="3" y="1.5" width="10" height="8" fill="none" stroke="#ddd" stroke-width="1"/><path d="M3 1.5l5 4 5-4" fill="none" stroke="#ddd"/><path d="M0 3h2M0 5.5h2" stroke="#ddd"/></svg>
    <span>support@brightmarkpixelcollective.com</span>
  </div>
  <div class="item" style="left:322px">
    <svg viewBox="0 0 14 11"><path d="M3 1c1 0 2 2 2 3s-1 1 0 2 2 2 3 1 3 1 3 2-2 2-3 1S2 6 2 3s0-2 1-2z" fill="#ddd"/></svg>
    <span>TOLL FREE: 1-800-555-0142</span>
    <span style="margin-left:8px">Local: 612-555-0187</span>
  </div>
</div>

<header class="abs site-header">
  <div class="brand">
    <span class="brand-mark"></span>
    <span class="brand-name">Brightmark Pixel Collective</span>
  </div>
  <nav class="nav">
    <a class="active" style="left:429px">Home</a>
    <a style="left:486px">Services<span class="caret"></span></a>
    <a style="left:552px">Portfolio<span class="caret"></span></a>
    <a style="left:620px">About Us<span class="caret"></span></a>
    <a style="left:691px">Blog</a>
    <a style="left:741px">Contact</a>
  </nav>
</header>

<div class="abs hero" role="img" aria-label="Photo of a team working at desks in a bright open office"></div>
<div class="abs hero-shade"></div>
<h1 class="abs hero-title">We Provide<br>Website Design and Development<br>for Grouth of Your Business</h1>
<div class="abs hero-btn">Learn More</div>

<section class="abs welcome"></section>
<h2 class="abs section-title welcome-title">Welcome to Brightmark Pixel Collective</h2>
<p class="abs welcome-lead">Maecenas bibendum lacus gravida placerat consequat. Vivamus quis hendrerit mauris. Vestibulum laoreet felis sed consectetur sollicitudin.</p>

<article class="abs card" style="left:123px">
  <div class="card-photo" role="img" aria-label="Photo of business people meeting around a table" style="background:linear-gradient(135deg,#cfe4ec,#8fb3c4 60%,#5d7d8e)"></div>
  <h3 class="card-title">Our Mission</h3>
  <p class="card-text">Lorem ipsum dolor sit amet, consectetur adipisicing elit, sed do eiusmod tempor incididunt ut labore et dolore magna aliqua.</p>
</article>
<article class="abs card featured" style="left:343px">
  <div class="card-photo" role="img" aria-label="Photo of a team looking at a tablet together" style="background:linear-gradient(135deg,#f2f2f2,#cfcac4 55%,#8e8680)">
    <span class="plus">+</span>
    <span class="corner"></span>
  </div>
  <h3 class="card-title">Our Values</h3>
  <p class="card-text">Lorem ipsum dolor sit amet, consectetur adipisicing elit, sed do eiusmod tempor incididunt ut labore et dolore magna aliqua.</p>
</article>
<article class="abs card" style="left:564px">
  <div class="card-photo" role="img" aria-label="Photo of hands holding a blue cloud" style="background:radial-gradient(circle at 50% 45%,#3d8ee0,#8fc0ef 55%,#eef4fa)"></div>
  <h3 class="card-title">Our Solution</h3>
  <p class="card-text">Lorem ipsum dolor sit amet, consectetur adipisicing elit, sed do eiusmod tempor incididunt ut labore et dolore magna aliqua.</p>
</article>

<h2 class="abs section-title experts-title">We're experts in</h2>

<article class="abs expert" style="left:116px">
  <div class="expert-icon">
    <svg viewBox="0 0 32 32"><circle cx="12" cy="18" r="7" fill="none" stroke="#f7a81b" stroke-width="4" stroke-dasharray="3 2.5"/><circle cx="12" cy="18" r="4" fill="none" stroke="#f7a81b" stroke-width="2.5"/><circle cx="23" cy="9" r="4.5" fill="none" stroke="#f7a81b" stroke-width="3" stroke-dasharray="2 2"/><circle cx="23" cy="23" r="4.5" fill="none" stroke="#f7a81b" stroke-width="3" stroke-dasharray="2 2"/></svg>
  </div>
  <h3 class="expert-title">Web Development</h3>
  <p class="expert-text">Lorem ipsum dolor sit amet, consectetuer adipiscing elit. Aenean commodo ligula eget dolor. Aenean massa. Cum sociis natoque penatibus et magnis dis parturient montes, nascetur ridiculus mus.</p>
  <span class="expert-btn">LEARN MORE</span>
</article>
<article class="abs expert" style="left:281px">
  <div class="expert-icon">
    <svg viewBox="0 0 32 32"><path d="M11 12l5-6 5 6" fill="none" stroke="#f7a81b" stroke-width="2"/><rect x="4" y="12" width="24" height="4" fill="#f7a81b"/><path d="M6 17h20l-2 9H8z" fill="#f7a81b"/><path d="M9 20h14M10 23h12" stroke="#2b2b2b" stroke-width="1.5"/></svg>
  </div>
  <h3 class="expert-title">Amazing Online Stores</h3>
  <p class="expert-text">Lorem ipsum dolor sit amet, consectetuer adipiscing elit. Aenean commodo ligula eget dolor. Aenean massa. Cum sociis natoque penatibus et magnis dis parturient montes, nascetur ridiculus mus.</p>
  <span class="expert-btn">LEARN MORE</span>
</article>
<article class="abs expert featured" style="left:447px">
  <div class="expert-icon">
    <svg viewBox="0 0 32 32"><path d="M6 8h20a2 2 0 0 1 2 2v10a2 2 0 0 1-2 2H14l-6 5v-5H6a2 2 0 0 1-2-2V10a2 2 0 0 1 2-2z" fill="#2b2b2b"/></svg>
  </div>
  <h3 class="expert-title">Social Media</h3>
  <p class="expert-text">Lorem ipsum dolor sit amet, consectetuer adipiscing elit. Aenean commodo ligula eget dolor. Aenean massa. Cum sociis natoque penatibus et magnis dis parturient montes, nascetur ridiculus</p>
  <span class="expert-btn">LEARN MORE</span>
</article>
<article class="abs expert" style="left:611px">
  <div class="expert-icon">
    <svg viewBox="0 0 32 32"><rect x="4" y="5" width="24" height="22" fill="none" stroke="#f7a81b" stroke-width="2.5"/><rect x="9" y="16" width="3" height="7" fill="#f7a81b"/><rect x="14.5" y="12" width="3" height="11" fill="#f7a81b"/><rect x="20" y="9" width="3" height="14" fill="#f7a81b"/></svg>
  </div>
  <h3 class="expert-title">Online Marketing</h3>
  <p class="expert-text">Lorem ipsum dolor sit amet, consectetuer adipiscing elit. Aenean commodo ligula eget dolor. Aenean massa. Cum sociis natoque penatibus et magnis dis parturient montes,</p>
  <span class="expert-btn">LEARN MORE</span>
</article>

<div class="abs footer-band"></div>
</body>
</html>
```